Custom Cabinet Shop Needs a website design

Hi,
We need a website for a Custom Cabinet Shop and Cabinet parts manufacturing business.
The business has two sides to it. One side provides custom Kitchens, vanities, entertainment units, offices and what not to homeowners and contractors.
The 2nd side of the business provides built to order cabinet boxes and other parts required to put together a project to other cabinet shops, small contractors looking to install there own cabinets.
Website will need a Gallery to display work.
Color scheme to go well with logo.
current website is www.brindlewoodcustomcabinets.com
being changed to www.brindlewood.ca
Logo Included in attached files.
Tagline "Millwork with Flare"
Mission Statement "Our passion is to deliver inspired cabinetry solutions to suit all your needs, supported by our phenomenal star class customer service"
The website should convey quality and professionalism.
Thank you.
Homeowners/ Contractors
Entertainment
Coded - Design and coding required
1 page

```html
<!DOCTYPE html>
<html lang="en">
<head>
<meta charset="utf-8">
<title>Brindlewood Custom Cabinets</title>
<link rel="stylesheet" href="https://fonts.googleapis.com/css2?family=Lato:wght@300;400;700&display=swap">
<style>
  :root {
    --ink: #1a1a1a;
    --text: #333333;
    --muted: #555555;
    --accent: #f15a24;
    --rule: #d6d6d6;
    --footer-bg: #ebebeb;
    --white: #ffffff;
  }
  * { box-sizing: border-box; margin: 0; padding: 0; }
  html, body { width: 1120px; height: 1200px; overflow: hidden; }
  body {
    position: relative;
    background: var(--white);
    font-family: "Lato", sans-serif;
    font-weight: 300;
    color: var(--text);
  }

  /* Header */
  .site-header { position: absolute; left: 0; top: 0; width: 1120px; height: 110px; background: var(--white); }
  .brand {
    position: absolute; left: 162px; top: 34px;
    display: flex; align-items: center; gap: 10px;
    font-weight: 700; font-size: 24px; letter-spacing: 1px; color: var(--ink);
    text-decoration: none;
  }
  .brand-mark { width: 26px; height: 26px; border-radius: 50%; background: var(--accent); }
  .main-nav { position: absolute; left: 397px; top: 32px; height: 44px; display: flex; }
  .main-nav a {
    display: flex; align-items: center; justify-content: center;
    width: 112px; height: 44px;
    border-left: 1px solid var(--rule);
    font-size: 11px; font-weight: 400; color: var(--ink);
    text-decoration: none; text-transform: uppercase;
  }
  .main-nav a.is-active { color: var(--accent); }

  /* Hero */
  .hero {
    position: absolute; left: 0; top: 110px; width: 1120px; height: 586px;
    background:
      radial-gradient(ellipse at 75% 20%, rgba(255,240,210,.55), transparent 45%),
      linear-gradient(180deg, #d8d2c8 0%, #b9b2a7 35%, #8c8378 62%, #5a4e44 100%);
  }
  .hero-frame {
    position: absolute; left: 284px; top: 219px; width: 555px; height: 148px;
    border: 1px solid rgba(255,255,255,.85);
  }
  .hero-panel {
    position: absolute; left: 298px; top: 235px; width: 528px; height: 117px;
    background: rgba(255,255,255,.62);
    display: flex; align-items: center; justify-content: center;
  }
  .hero-tagline {
    font-weight: 300; font-size: 38px; letter-spacing: 4px;
    color: var(--ink); text-transform: uppercase; white-space: nowrap;
  }
  .slider-dots { position: absolute; left: 513px; top: 542px; display: flex; gap: 8px; }
  .slider-dots span { width: 12px; height: 12px; border-radius: 50%; border: 1.5px solid var(--white); }
  .slider-dots span.is-current { background: var(--white); }

  /* Mission */
  .mission { position: absolute; left: 0; top: 740px; width: 1120px; text-align: center; }
  .mission-title { font-weight: 300; font-size: 38px; letter-spacing: 3px; color: var(--ink); line-height: 56px; }
  .mission-rule { width: 112px; height: 1px; background: #888; margin: 8px auto 0; }
  .mission-text {
    margin-top: 18px; font-size: 18.5px; font-weight: 300; letter-spacing: 1.6px;
    line-height: 29px; color: var(--muted);
  }
  .btn-outline {
    display: inline-block; margin-top: 31px;
    width: 157px; height: 44px; line-height: 42px;
    border: 1px solid var(--ink);
    font-size: 12px; font-weight: 400; letter-spacing: 2px; color: var(--ink);
    text-decoration: none; text-transform: uppercase;
  }

  /* Footer */
  .site-footer { position: absolute; left: 0; top: 1051px; width: 1120px; height: 149px; background: var(--footer-bg); }
  .footer-nav { position: absolute; left: 162px; top: 35px; display: flex; font-size: 11px; font-weight: 400; }
  .footer-nav a { color: var(--ink); text-decoration: none; text-transform: uppercase; }
  .footer-nav .sep { color: #999; margin: 0 12px; }
  .footer-contact {
    position: absolute; left: 162px; top: 65px;
    display: flex; align-items: center; gap: 10px;
    font-size: 12.5px; font-weight: 400; color: var(--ink);
  }
  .contact-item { display: flex; align-items: center; gap: 6px; }
  .contact-icon { width: 15px; height: 15px; }
  .social-list { display: flex; gap: 2px; margin-left: 2px; }
  .social-list span { width: 18px; height: 18px; border-radius: 50%; background: var(--ink); }
  .copyright { position: absolute; left: 162px; top: 98px; font-size: 10.5px; color: var(--muted); }
  .footer-brand { left: 734px; top: 1051px; position: absolute; margin-top: 55px; }
</style>
</head>
<body>
  <header class="site-header">
    <a class="brand" href="#"><span class="brand-mark"></span>BRINDLEWOOD</a>
    <nav class="main-nav">
      <a class="is-active" href="#">Home</a>
      <a href="#">Gallery</a>
      <a href="#">Services</a>
      <a href="#">Warranty</a>
      <a href="#">Contact</a>
    </nav>
  </header>

  <section class="hero" role="img" aria-label="Photo of a bright custom kitchen with white cabinets, stainless hood and appliances, and a granite island">
    <div class="hero-frame"></div>
    <div class="hero-panel"><h1 class="hero-tagline">Millwork with Flare</h1></div>
    <div class="slider-dots">
      <span class="is-current"></span><span></span><span></span><span></span><span></span>
    </div>
  </section>

  <section class="mission">
    <h2 class="mission-title">Our Mission</h2>
    <div class="mission-rule"></div>
    <p class="mission-text">Our passion is to deliver inspired cabinetry solutions to suit all your needs,<br>supported by our phenomenal star class customer service</p>
    <a class="btn-outline" href="#">Visit our work</a>
  </section>

  <footer class="site-footer">
    <nav class="footer-nav">
      <a href="#">Home</a><span class="sep">|</span>
      <a href="#">Gallery</a><span class="sep">|</span>
      <a href="#">Services</a><span class="sep">|</span>
      <a href="#">Warranty</a><span class="sep">|</span>
      <a href="#">Contact</a>
    </nav>
    <div class="footer-contact">
      <span class="contact-item">
        <svg class="contact-icon" viewBox="0 0 16 16" aria-hidden="true"><circle cx="8" cy="8" r="8" fill="#f15a24"/><path d="M5.2 4.2l1.4-.2.8 2-1 .8c.5 1.1 1.3 1.9 2.4 2.4l.8-1 2 .8-.2 1.4c-3.5.3-6.5-2.7-6.2-6.2z" fill="#fff"/></svg>
        403-555-0148
      </span>
      <span class="contact-item">
        <svg class="contact-icon" viewBox="0 0 16 16" aria-hidden="true"><circle cx="8" cy="8" r="8" fill="#f15a24"/><rect x="4" y="5" width="8" height="6" rx=".5" fill="#fff"/><path d="M4.3 5.4L8 8.3l3.7-2.9" stroke="#f15a24" stroke-width="1" fill="none"/></svg>
        sales@brindlewoodcustomcabinets.com
      </span>
      <span class="social-list" aria-label="Social links"><span></span><span></span><span></span></span>
    </div>
    <p class="copyright">©copyright 2015. All rights reserved</p>
  </footer>
  <a class="brand footer-brand" href="#"><span class="brand-mark"></span>BRINDLEWOOD</a>
</body>
</html>
```